Crestline Decor Depot needs Business cards and letterhead

letterhead, envelope & business card
Letterhead:
Crestline Decor Depot
4823 Larkfield Drive Ridgeview, ND 59744
Phone #: (555) 555-0148
Fax#: (555) 555-0192
Business cards:
Crestline Decor Depot
Phone #: (555) 555-0148
Fax#: (555) 555-0192
Corinne Vasko
corinne@crestlinedecordepot.example
www.crestlinedecordepot.example
Target Market(s)
Home Interiors client
Industry/Entity Type
Business
Requirements
Must have
- ONLY submit straight front view on white background
- I DO NOT WANT ANY MOCK UPS
Nice to have
- see attached logo use guide
Should not have

```html
<!DOCTYPE html>
<html lang="en">
<head>
<meta charset="utf-8">
<title>Crestline Decor Depot – Stationery</title>
<link href="https://fonts.googleapis.com/css2?family=Source+Sans+3:wght@400;600&display=swap" rel="stylesheet">
<style>
  :root {
    --brand-blue: #1672c0;
    --brand-grey: #6b6b6d;
    --ink: #3a3a3a;
    --ink-soft: #555;
    --paper: #ffffff;
    --canvas: #ffffff;
    --edge: #e2e2e2;
  }
  * { margin: 0; padding: 0; box-sizing: border-box; }
  html, body { width: 1200px; height: 876px; overflow: hidden; }
  body {
    background: var(--canvas);
    font-family: "Source Sans 3", sans-serif;
    color: var(--ink);
    position: relative;
  }
  .sheet {
    position: absolute;
    background: var(--paper);
    border: 1px solid var(--edge);
    overflow: hidden;
  }
  .brand-bar { position: absolute; left: 0; right: 0; bottom: 0; }
  .wordmark {
    position: absolute;
    display: flex; align-items: center; gap: 5px;
    font-weight: 600; color: var(--ink-soft);
    text-transform: uppercase; letter-spacing: 0.04em;
    white-space: nowrap;
  }
  .wordmark .mark-square { width: 8px; height: 8px; background: var(--brand-blue); flex: none; }

  /* Letterhead */
  .letterhead { left: 101px; top: 118px; width: 470px; height: 604px; }
  .letterhead .wordmark { left: 38px; top: 62px; font-size: 10px; }
  .letterhead .brand-bar { height: 8px; background: linear-gradient(100deg, var(--brand-blue) 0 50%, var(--brand-grey) 50% 100%); }
  .letterhead-contact {
    position: absolute; left: 319px; top: 36px; height: 58px;
    border-left: 1px solid var(--brand-blue); padding-left: 14px;
    font-size: 5.6px; line-height: 6.6px; color: var(--ink-soft);
  }
  .letterhead-contact .company { color: var(--brand-blue); font-weight: 600; font-size: 7.8px; line-height: 8px; }
  .letterhead-contact .contact-list { margin-top: 6px; list-style: none; }
  .contact-list li { display: flex; align-items: center; gap: 4px; }
  .contact-list svg { width: 5px; height: 5px; fill: var(--brand-blue); flex: none; }
  .letter-body {
    position: absolute; left: 74px; top: 134px; width: 366px;
    font-size: 8.2px; line-height: 12.6px; color: var(--ink-soft); font-weight: 400;
  }
  .letter-date { margin-bottom: 14px; }
  .letter-recipient { line-height: 10px; margin-bottom: 26px; }
  .letter-body p.para { text-align: justify; margin-bottom: 12.6px; }
  .signature { margin-top: 34px; }
  .signature .signer { font-size: 12px; line-height: 14px; }
  .signature .role { font-size: 7.4px; line-height: 12px; }

  /* Business card front */
  .card-front { left: 642px; top: 117px; width: 217px; height: 125px; }
  .card-front .wordmark { left: 15px; top: 30px; font-size: 6.6px; gap: 4px; }
  .card-front .wordmark .mark-square { width: 6px; height: 6px; }
  .card-front .brand-bar { height: 5px; background: linear-gradient(95deg, var(--brand-blue) 0 51%, var(--brand-grey) 51% 100%); }
  .card-person { position: absolute; left: 15px; top: 64px; width: 186px; border-bottom: 0.8px solid var(--brand-blue); padding-bottom: 2px; }
  .card-person .name { color: var(--brand-blue); font-weight: 600; font-size: 7.6px; line-height: 8px; }
  .card-person .title { font-size: 4.6px; line-height: 6px; color: var(--ink-soft); }
  .card-front .contact-list {
    position: absolute; left: 15px; top: 86px; list-style: none;
    font-size: 4.6px; line-height: 5.6px; color: var(--ink-soft);
  }
  .card-front .contact-list svg { width: 4px; height: 4px; }
  .card-address {
    position: absolute; right: 15px; top: 101px; text-align: right;
    font-size: 4.6px; line-height: 5.6px; color: var(--ink-soft);
  }

  /* Business card back */
  .card-back { left: 875px; top: 117px; width: 209px; height: 125px; background: var(--brand-blue); border-color: var(--brand-blue); }
  .card-back .wordmark { left: 0; right: 0; top: 56px; justify-content: center; color: #fff; font-size: 9px; }
  .card-back .wordmark .mark-square { background: #fff; }

  /* Envelope back */
  .envelope-back { left: 639px; top: 294px; width: 446px; height: 200px; }
  .envelope-flap { position: absolute; left: 0; top: 0; width: 446px; height: 56px; }
  .envelope-back .wordmark { left: 0; right: 0; top: 21px; justify-content: center; color: #fff; font-size: 7.5px; }
  .envelope-back .wordmark .mark-square { background: #fff; width: 7px; height: 7px; }

  /* Envelope front */
  .envelope-front { left: 642px; top: 525px; width: 445px; height: 203px; }
  .envelope-front .wordmark { left: 24px; top: 44px; font-size: 7.8px; }
  .envelope-front .wordmark .mark-square { width: 7px; height: 7px; }
  .envelope-front .brand-bar { height: 7px; background: linear-gradient(98deg, var(--brand-blue) 0 50%, var(--brand-grey) 50% 100%); }
  .return-address { position: absolute; left: 25px; top: 67px; font-size: 4.8px; line-height: 5.8px; color: var(--ink-soft); }
  .return-address .company { color: var(--brand-blue); font-weight: 600; font-size: 7.2px; line-height: 8px; }
</style>
</head>
<body>

<svg width="0" height="0" style="position:absolute">
  <defs>
    <symbol id="icon-phone" viewBox="0 0 10 10"><path d="M2 0.5 L3.6 2.6 L2.8 3.6 C3.4 5 5 6.6 6.4 7.2 L7.4 6.4 L9.5 8 L8.4 9.5 C4.6 9.2 0.8 5.4 0.5 1.6 Z"/></symbol>
    <symbol id="icon-fax" viewBox="0 0 10 10"><path d="M2.5 0.5 H7.5 V3 H2.5 Z M0.5 3.5 H9.5 V8 H7.5 V9.5 H2.5 V8 H0.5 Z M3.5 6.5 V8.5 H6.5 V6.5 Z"/></symbol>
    <symbol id="icon-mail" viewBox="0 0 10 10"><path d="M0.5 2 H9.5 V8 H0.5 Z M1 2.4 L5 5.4 L9 2.4" /></symbol>
    <symbol id="icon-web" viewBox="0 0 10 10"><circle cx="5" cy="5" r="4.5"/></symbol>
  </defs>
</svg>

<!-- Letterhead -->
<section class="sheet letterhead">
  <div class="wordmark"><span class="mark-square"></span>Crestline Decor Depot</div>
  <div class="letterhead-contact">
    <div class="company">Crestline Decor Depot</div>
    <div>4823 Larkfield Drive</div>
    <div>Ridgeview, ND 59744</div>
    <ul class="contact-list">
      <li><svg><use href="#icon-phone"/></svg>(555) 555-0148</li>
      <li><svg><use href="#icon-fax"/></svg>(555) 555-0192</li>
      <li><svg><use href="#icon-mail"/></svg>corinne@crestlinedecordepot.example</li>
      <li><svg><use href="#icon-web"/></svg>www.crestlinedecordepot.example</li>
    </ul>
  </div>
  <div class="letter-body">
    <p class="letter-date">March 26, 2018</p>
    <p class="letter-recipient">Dear Mr. Smith,<br>demo street,<br>demo placeP.O.<br>Box 000, 555 Avenue</p>
    <p class="para">Lorem ipsum dolor sit amet, consectetur adipiscing elit. Donec orci purus, luctus vitae dignissim eu, iaculis sed purus. Vivamus faucibus, ipsum nec aliquet viverra, leo mauris condimentum ligula, sit amet sagittis enim ligula quis arcu. Nam egestas tortor id nisi porttitor mattis. In tortor ante, ultricies in suscipit a, tempus non massa. Vivamus et auctor mi. Fusce vel massa nulla. Phasellus nec eros mauris, et scelerisque orci. Donec malesuada orci vitae nulla accumsan porta a id massa. Quisque accumsan iaculis magna sit amet fringilla. Maecenas consequat, magna eget tincidunt semper, odio nibh rutrum mi, id feugiat ante nisi eu risus. Vestibulum nunc orci, rhoncus a placerat in, ultricies in mi. Cras mattis varius eros, vel fringilla nisi suscipit eget.</p>
    <p class="para">Quisque scelerisque sagittis nulla at porttitor. Mauris a justo et tellus interdum tristique. Sed id augue vitae urna euismod commodo aliquet a quam. Pellentesque arcu velit, cursus et malesuada ut, consequat et diam. Nullam erat sem, rhoncus id ullamcorper vitae, rhoncus et arcu. In ultricies ultricies nulla, ut rutrum nisi iaculis at. Donec eu magna a metus ornare faucibus. Fusce aliquet faucibus ultricies. Morbi semper, est id tincidunt gravida, sem arcu adipiscing lacus, ac bibendum nulla leo eu purus. Quisque nec diam sed risus consectetur a ccumsan quis quis nibh. Vestibulum id purus lorem.</p>
    <div class="signature">
      <p class="signer">John Doe</p>
      <p class="role">Co-Founder &amp; CEO</p>
    </div>
  </div>
  <div class="brand-bar"></div>
</section>

<!-- Business card front -->
<section class="sheet card-front">
  <div class="wordmark"><span class="mark-square"></span>Crestline Decor Depot</div>
  <div class="card-person">
    <div class="name">Corinne Vasko</div>
    <div class="title">Designation</div>
  </div>
  <ul class="contact-list">
    <li><svg><use href="#icon-phone"/></svg>(555) 555-0148</li>
    <li><svg><use href="#icon-fax"/></svg>(555) 555-0192</li>
    <li><svg><use href="#icon-mail"/></svg>corinne@crestlinedecordepot.example</li>
    <li><svg><use href="#icon-web"/></svg>www.crestlinedecordepot.example</li>
  </ul>
  <div class="card-address">4823 Larkfield Drive<br>Ridgeview, ND 59744</div>
  <div class="brand-bar"></div>
</section>

<!-- Business card back -->
<section class="sheet card-back">
  <div class="wordmark"><span class="mark-square"></span>Crestline Decor Depot</div>
</section>

<!-- Envelope back -->
<section class="sheet envelope-back">
  <svg class="envelope-flap" viewBox="0 0 446 56" aria-hidden="true">
    <path d="M0 0 H446 L438 44 Q436 56 422 56 H26 Q12 56 9 44 Z" fill="var(--brand-blue)"/>
  </svg>
  <div class="wordmark"><span class="mark-square"></span>Crestline Decor Depot</div>
</section>

<!-- Envelope front -->
<section class="sheet envelope-front">
  <div class="wordmark"><span class="mark-square"></span>Crestline Decor Depot</div>
  <div class="return-address">
    <div class="company">Crestline Decor Depot</div>
    <div>4823 Larkfield Drive</div>
    <div>Ridgeview, ND 59744</div>
  </div>
  <div class="brand-bar"></div>
</section>

</body>
</html>
```